Scrap Metal Recycling

We are looking for a simple yet bold business card. We already have the logo, please see attached. Color scheme of blue, black and white or just blue and white.

```html
<!DOCTYPE html>
<html lang="en">
<head>
<meta charset="utf-8">
<title>Harbor Line Metals – Business Card</title>
<link href="https://fonts.googleapis.com/css2?family=Source+Sans+3:wght@400;600;700&display=swap" rel="stylesheet">
<style>
  :root {
    --page-bg: #d9d9d9;
    --card-dark: #2b2b2b;
    --card-band: #3a3a3a;
    --divider: #7a7a7a;
    --brand-blue: #1b86ab;
    --text-white: #ffffff;
    --text-light: #e6e6e6;
    --pattern-light: #5c5c5c;
    --pattern-dark: #1c1c1c;
  }
  * { box-sizing: border-box; margin: 0; padding: 0; }
  html, body {
    width: 1200px; height: 960px; overflow: hidden;
    background: var(--page-bg);
    font-family: "Source Sans 3", Arial, sans-serif;
  }
  .canvas { position: relative; width: 1200px; height: 960px; }
  .card {
    position: absolute; left: 298px; width: 610px; height: 348px;
    overflow: hidden;
  }
  .card-front { top: 107px; background: var(--card-dark); }
  .card-back { top: 510px; background: var(--card-dark); }

  .front-texture {
    position: absolute; inset: 0;
    background: linear-gradient(135deg, var(--pattern-light) 0%, #3a3a3a 45%, var(--pattern-dark) 100%);
  }
  .brand-block {
    position: absolute; left: 0; right: 0; text-align: center;
  }
  .card-front .brand-block { top: 150px; }
  .brand-name {
    color: var(--text-white); font-weight: 600;
    font-size: 46px; line-height: 1; letter-spacing: 1px;
    text-transform: uppercase;
  }
  .brand-tagline {
    color: var(--brand-blue); font-weight: 600;
    font-size: 21px; letter-spacing: 5px; margin-top: 8px;
    text-transform: uppercase;
  }
  .card-back .brand-name { font-size: 50px; }
  .card-back .brand-tagline { font-size: 24px; letter-spacing: 5.5px; }

  .back-band {
    position: absolute; left: 0; top: 0; width: 100%; height: 175px;
    background: var(--card-band);
    border-bottom: 2px solid var(--divider);
  }
  .card-back .brand-block { top: 62px; }

  .person { position: absolute; left: 48px; top: 240px; }
  .person-name {
    color: var(--brand-blue); font-weight: 700; font-size: 19px; letter-spacing: 0.3px;
  }
  .person-title { color: var(--text-light); font-size: 15px; margin-top: 2px; }

  .contact { position: absolute; left: 386px; top: 204px; color: var(--text-light); font-size: 15px; line-height: 19px; }
  .contact-address { margin-bottom: 15px; }
  .contact-line { display: flex; align-items: center; gap: 5px; }
  .contact-line svg { width: 14px; height: 14px; flex: none; }
</style>
</head>
<body>
<div class="canvas">

  <section class="card card-front">
    <div class="front-texture" role="img" aria-label="Repeating brand symbol pattern in glossy greys on black"></div>
    <div class="brand-block">
      <div class="brand-name">Harbor Line Metals</div>
      <div class="brand-tagline">Scrap Metal Recycling</div>
    </div>
  </section>

  <section class="card card-back">
    <div class="back-band"></div>
    <div class="brand-block">
      <div class="brand-name">Harbor Line Metals</div>
      <div class="brand-tagline">Scrap Metal Recycling</div>
    </div>

    <div class="person">
      <div class="person-name">DANIEL MERCER</div>
      <div class="person-title">Founder &amp; Owner</div>
    </div>

    <div class="contact">
      <div class="contact-address">418 Dock Street<br>Fairhaven, CT 06512</div>
      <div class="contact-line">
        <svg viewBox="0 0 16 16" aria-hidden="true"><path d="M3.5 1.5l2.5 2.8-1.4 1.8c.9 2 2.4 3.5 4.3 4.4l1.8-1.4 2.8 2.5-1.5 2c-5.5-.5-9.6-4.6-10.1-10.1z" fill="#1b86ab"/></svg>
        <span>(203) 555-0147</span>
      </div>
      <div class="contact-line">
        <svg viewBox="0 0 16 16" aria-hidden="true"><rect x="1.5" y="3.5" width="13" height="9" fill="none" stroke="#1b86ab" stroke-width="1.5"/><path d="M1.5 3.5L8 9l6.5-5.5" fill="none" stroke="#1b86ab" stroke-width="1.5"/></svg>
        <span>info@harborlinemetals.com</span>
      </div>
      <div class="contact-line">
        <svg viewBox="0 0 16 16" aria-hidden="true"><circle cx="8" cy="8" r="6.2" fill="none" stroke="#1b86ab" stroke-width="1.4"/><ellipse cx="8" cy="8" rx="2.6" ry="6.2" fill="none" stroke="#1b86ab" stroke-width="1.2"/><path d="M1.8 8h12.4" stroke="#1b86ab" stroke-width="1.2"/></svg>
        <span>www.harborlinemetals.com</span>
      </div>
    </div>
  </section>

</div>
</body>
</html>
```